Mediation service showing compassion, collaboration, and resolution

I would like to purchase a customized version of a design you have previously submitted - https://www.pixelbidhub.com/design/48172635

Hello,

I would like a design for a flyer for my mediation business.
I also want to include a message that says that I offer rates on sliding scale.
My website is: www.morvantelkresolve.com

Let me know what other details you might want?

Thank you,

Teodric

Target Market(s)

Local community, western Massachusetts USA. Businesses, families, individuals.

Industry/Entity Type

Mediation, Legal, Alternative Dispute Resolution, Divorce, Unions

Font styles to use
Sans Serif

Colors
0094D4
00A9DD
6FCCEA
C7EBF8
E9F6FB
00AB8E
00BBA5
67D7C9
C6EFE9
E9F9F6

Requirements
Must have
• “Sliding scale rates available “. Phone and email details. +1.555.384.7290 and email: teodric@morvantelkresolve.com as well as we code to my website www.morvantelkresolve.com

```html
<!DOCTYPE html>
<html lang="en">
<head>
<meta charset="utf-8">
<title>Teodric Morvantelk – Mediation Flyer</title>
<link href="https://fonts.googleapis.com/css2?family=Montserrat:wght@300;400;500;600;700;800&display=swap" rel="stylesheet">
<style>
  :root {
    --teal: #2f9b8f;
    --teal-dark: #23887e;
    --blue: #1d6da0;
    --blue-deep: #1a5f8e;
    --ink: #1f2a33;
    --muted: #39444d;
    --paper: #f3f4f4;
    --stage: #e4e7e8;
    --gold: #f6b52e;
    --white: #ffffff;
  }
  * { box-sizing: border-box; margin: 0; padding: 0; }
  html, body { width: 696px; height: 1200px; overflow: hidden; }
  body {
    background: var(--stage);
    font-family: "Montserrat", Arial, sans-serif;
    color: var(--ink);
    position: relative;
  }
  .flyer {
    position: absolute;
    left: 18px; top: 175px;
    width: 660px; height: 850px;
    background: var(--paper);
    overflow: hidden;
    box-shadow: 0 6px 22px rgba(0,0,0,.18);
  }
  .abs { position: absolute; }

  /* header */
  .brand-name { left: 30px; top: 36px; font-size: 25px; font-weight: 500; color: var(--ink); letter-spacing: .2px; }
  .brand-tag { left: 106px; top: 72px; font-size: 9px; font-weight: 600; color: var(--ink); letter-spacing: .4px; }
  .site { right: 30px; top: 34px; font-size: 19px; font-weight: 500; color: var(--ink); }
  .site-rule { right: 30px; top: 62px; width: 50px; height: 2px; background: var(--blue); }
  .address { right: 30px; top: 74px; font-size: 9.5px; color: var(--ink); display: flex; align-items: center; gap: 4px; }

  /* hero */
  .hero-band {
    left: 0; top: 119px; width: 660px; height: 245px;
    background: linear-gradient(90deg, var(--teal) 0%, var(--teal) 40%, var(--blue) 100%);
  }
  .hero-photo {
    left: 300px; top: 119px; width: 360px; height: 245px;
    background: radial-gradient(ellipse at 60% 55%, rgba(47,127,176,.95) 0%, rgba(37,110,156,.8) 50%, rgba(37,110,156,0) 85%);
  }
  .hero-title { left: 43px; top: 142px; font-size: 28px; font-weight: 700; line-height: 1.18; color: var(--white); }
  .hero-sub { left: 43px; top: 252px; font-size: 17px; font-weight: 300; line-height: 1.25; color: var(--white); }

  /* services */
  .services-title { left: 43px; top: 382px; font-size: 18px; font-weight: 500; color: var(--ink); }
  .dots { left: 43px; top: 409px; display: flex; gap: 3px; }
  .dots span { width: 5px; height: 5px; border-radius: 50%; background: var(--blue); }
  .dots span:nth-child(2) { background: #3a82ad; }
  .dots span:nth-child(3) { background: #7aaccb; }
  .dots span:nth-child(4) { background: #c3d8e6; }
  .service-list { list-style: none; font-size: 10px; line-height: 1.22; color: var(--muted); }
  .service-list li { display: flex; gap: 7px; margin-bottom: 5.5px; }
  .service-list span { white-space: nowrap; }
  .service-list svg { flex: none; margin-top: 2px; }
  .list-left { left: 43px; top: 427px; width: 220px; }
  .list-right { left: 268px; top: 427px; width: 148px; }

  /* mediation note */
  .note {
    left: 421px; top: 476px; width: 205px; height: 196px;
    border: 2.5px solid var(--blue); border-radius: 10px; background: var(--white);
  }
  .note-label {
    left: 442px; top: 464px; width: 164px; height: 25px;
    background: linear-gradient(90deg, var(--teal), var(--blue));
    border-radius: 4px; color: var(--white); font-size: 16px; font-weight: 500;
    text-align: center; line-height: 25px;
  }
  .note-text { left: 431px; top: 502px; width: 185px; font-size: 10.6px; line-height: 1.36; text-align: center; color: var(--ink); }

  /* profile */
  .profile-band {
    left: 0; top: 654px; width: 660px; height: 97px;
    background: linear-gradient(90deg, var(--teal) 0%, var(--blue) 55%, var(--blue-deep) 100%);
  }
  .headshot {
    left: 45px; top: 613px; width: 102px; height: 131px;
    border-radius: 8px; border: 3px solid var(--white);
    background: linear-gradient(180deg, #a3a7ab 0%, #8a7d74 55%, #b84a55 100%);
  }
  .connector { left: 140px; top: 610px; }
  .profile-name { left: 168px; top: 631px; font-size: 21px; font-weight: 500; color: var(--ink); }
  .profile-text { left: 168px; top: 664px; width: 220px; font-size: 10.4px; line-height: 1.25; color: var(--white); }
  .profile-text p + p { margin-top: 6px; }
  .offer-1 { left: 421px; top: 681px; font-size: 26px; font-weight: 700; color: var(--white); letter-spacing: .3px; }
  .offer-2 { left: 421px; top: 711px; font-size: 20.5px; font-weight: 600; color: var(--gold); letter-spacing: .2px; }

  /* footer */
  .role { left: 43px; top: 767px; font-size: 14px; font-weight: 500; line-height: 1.25; color: var(--ink); }
  .dynamics { left: 192px; top: 768px; list-style: none; font-size: 11.4px; font-weight: 500; color: var(--ink); }
  .dynamics li { display: flex; align-items: center; gap: 8px; margin-bottom: 4px; }
  .call-pill {
    left: 524px; top: 762px; width: 98px; height: 28px;
    background: linear-gradient(90deg, var(--teal), var(--teal-dark));
    border-radius: 6px; color: var(--white); font-size: 18px; font-weight: 700;
    text-align: center; line-height: 28px;
  }
  .phone { right: 38px; top: 796px; font-size: 19px; font-weight: 700; color: var(--ink); letter-spacing: .5px; }
  .email { right: 38px; top: 823px; font-size: 10px; font-weight: 500; color: var(--ink); }
</style>
</head>
<body>
<main class="flyer">
  <!-- header -->
  <div class="abs brand-name">Teodric V. Morvantelk</div>
  <div class="abs brand-tag">Alternative Dispute Resolution</div>
  <div class="abs site">www.morvantelkresolve.com</div>
  <div class="abs site-rule"></div>
  <div class="abs address">
    <svg width="7" height="10" viewBox="0 0 7 10"><path d="M3.5 0A3.5 3.5 0 0 0 0 3.5C0 6 3.5 10 3.5 10S7 6 7 3.5A3.5 3.5 0 0 0 3.5 0zm0 5a1.4 1.4 0 1 1 0-2.8 1.4 1.4 0 0 1 0 2.8z" fill="#1f2a33"/></svg>
    582 Larchmont Avenue #114, Westbrook MA 01089 USA
  </div>

  <!-- hero -->
  <div class="abs hero-band"></div>
  <div class="abs hero-photo" role="img" aria-label="Photo of a man and a woman meditating cross-legged in front of a blue mandala pattern"></div>
  <h1 class="abs hero-title">Mediation is a<br>form of facilitated<br>negotiation</h1>
  <p class="abs hero-sub">by a mediator, who<br>helps the parties engage<br>in a dialog to search for<br>a joint agreement.</p>

  <!-- services -->
  <h2 class="abs services-title">Services Provided</h2>
  <div class="abs dots"><span></span><span></span><span></span><span></span></div>

  <ul class="abs service-list list-left">
    <li><svg width="8" height="8" viewBox="0 0 8 8"><rect x=".5" y=".5" width="7" height="7" rx="1" fill="none" stroke="#1d6da0"/><path d="M2 4l1.5 1.5L6 2.5" fill="none" stroke="#1d6da0"/></svg><span>Divorce and Family Mediation<br>(Sliding scale rates)</span></li>
    <li><svg width="8" height="8" viewBox="0 0 8 8"><rect x=".5" y=".5" width="7" height="7" rx="1" fill="none" stroke="#1d6da0"/><path d="M2 4l1.5 1.5L6 2.5" fill="none" stroke="#1d6da0"/></svg><span>Commercial and business<br>related Mediation</span></li>
    <li><svg width="8" height="8" viewBox="0 0 8 8"><rect x=".5" y=".5" width="7" height="7" rx="1" fill="none" stroke="#1d6da0"/><path d="M2 4l1.5 1.5L6 2.5" fill="none" stroke="#1d6da0"/></svg><span>International business and<br>trading conflict mediation</span></li>
    <li><svg width="8" height="8" viewBox="0 0 8 8"><rect x=".5" y=".5" width="7" height="7" rx="1" fill="none" stroke="#1d6da0"/><path d="M2 4l1.5 1.5L6 2.5" fill="none" stroke="#1d6da0"/></svg><span>Merger Negotiations &amp;<br>Business Collaboration</span></li>
    <li><svg width="8" height="8" viewBox="0 0 8 8"><rect x=".5" y=".5" width="7" height="7" rx="1" fill="none" stroke="#1d6da0"/><path d="M2 4l1.5 1.5L6 2.5" fill="none" stroke="#1d6da0"/></svg><span>Mediation between dealer, agent,<br>distributor and supplier, manufacturer</span></li>
    <li><svg width="8" height="8" viewBox="0 0 8 8"><rect x=".5" y=".5" width="7" height="7" rx="1" fill="none" stroke="#1d6da0"/><path d="M2 4l1.5 1.5L6 2.5" fill="none" stroke="#1d6da0"/></svg><span>Contract negotiation consultancy</span></li>
  </ul>

  <ul class="abs service-list list-right">
    <li><svg width="8" height="8" viewBox="0 0 8 8"><rect x=".5" y=".5" width="7" height="7" rx="1" fill="none" stroke="#1d6da0"/><path d="M2 4l1.5 1.5L6 2.5" fill="none" stroke="#1d6da0"/></svg><span>Employment contract<br>negotiations</span></li>
    <li><svg width="8" height="8" viewBox="0 0 8 8"><rect x=".5" y=".5" width="7" height="7" rx="1" fill="none" stroke="#1d6da0"/><path d="M2 4l1.5 1.5L6 2.5" fill="none" stroke="#1d6da0"/></svg><span>Mediation for property or<br>entity division</span></li>
    <li><svg width="8" height="8" viewBox="0 0 8 8"><rect x=".5" y=".5" width="7" height="7" rx="1" fill="none" stroke="#1d6da0"/><path d="M2 4l1.5 1.5L6 2.5" fill="none" stroke="#1d6da0"/></svg><span>Workplace Mediation</span></li>
    <li><svg width="8" height="8" viewBox="0 0 8 8"><rect x=".5" y=".5" width="7" height="7" rx="1" fill="none" stroke="#1d6da0"/><path d="M2 4l1.5 1.5L6 2.5" fill="none" stroke="#1d6da0"/></svg><span>Mediation Coaching</span></li>
    <li><svg width="8" height="8" viewBox="0 0 8 8"><rect x=".5" y=".5" width="7" height="7" rx="1" fill="none" stroke="#1d6da0"/><path d="M2 4l1.5 1.5L6 2.5" fill="none" stroke="#1d6da0"/></svg><span>Ombuds contracting</span></li>
    <li><svg width="8" height="8" viewBox="0 0 8 8"><rect x=".5" y=".5" width="7" height="7" rx="1" fill="none" stroke="#1d6da0"/><path d="M2 4l1.5 1.5L6 2.5" fill="none" stroke="#1d6da0"/></svg><span>Mediation via<br>videoconference</span></li>
    <li><svg width="8" height="8" viewBox="0 0 8 8"><rect x=".5" y=".5" width="7" height="7" rx="1" fill="none" stroke="#1d6da0"/><path d="M2 4l1.5 1.5L6 2.5" fill="none" stroke="#1d6da0"/></svg><span>Meetings Facilitation</span></li>
  </ul>

  <!-- profile band -->
  <div class="abs profile-band"></div>

  <!-- mediation note -->
  <div class="abs note"></div>
  <div class="abs note-label">MEDIATION</div>
  <p class="abs note-text">The mediator has no authority over the parties nor impose any directives. The mediator is there to help the parties find their interests, list and organize the options they have vs the alternatives and the outcome probabilities for each outside a resolution via the mediation process.</p>

  <!-- profile -->
  <svg class="abs connector" width="24" height="30" viewBox="0 0 24 30"><path d="M0 3H14a6 6 0 0 1 6 6V24" fill="none" stroke="#1d6da0" stroke-width="1.2"/><circle cx="20" cy="26" r="2" fill="#1d6da0"/></svg>
  <div class="abs headshot" role="img" aria-label="Portrait photo of Teodric Morvantelk"></div>
  <div class="abs profile-name">Teodric Morvantelk</div>
  <div class="abs profile-text">
    <p>Working in the international business<br>world for over 30 years</p>
    <p>Teodric received his formal training<br>from LMI, one of the highest rated<br>mediation agencies in the nation</p>
  </div>
  <div class="abs offer-1">I OFFER RATES</div>
  <div class="abs offer-2">ON SLIDING SCALE</div>

  <!-- footer -->
  <p class="abs role">He sees his role as<br>managing three<br>dynamics:</p>
  <ul class="abs dynamics">
    <li><svg width="6" height="9" viewBox="0 0 6 9"><path d="M1 1l3.5 3.5L1 8" fill="none" stroke="#1d6da0" stroke-width="1.4"/></svg>the mediation process itself</li>
    <li><svg width="6" height="9" viewBox="0 0 6 9"><path d="M1 1l3.5 3.5L1 8" fill="none" stroke="#1d6da0" stroke-width="1.4"/></svg>the interaction between the parties</li>
    <li><svg width="6" height="9" viewBox="0 0 6 9"><path d="M1 1l3.5 3.5L1 8" fill="none" stroke="#1d6da0" stroke-width="1.4"/></svg>the issues and decisions facing the parties</li>
  </ul>
  <div class="abs call-pill">Call Us:</div>
  <div class="abs phone">555-384-7290</div>
  <div class="abs email">teodric@morvantelkresolve.com</div>
</main>
</body>
</html>
```